UPLIFT: Handwashing Poster (11x17)

- The poster will be 11x17.
- Attached is the general layout and language to be used. (attachment). Please feel to change the layout if there is a better use of space.
- It will use the same color theme as before - see example attachment one. (Less busy background).
- For final products, one poster will be branded 3 different ways (COVID-19, Flu, COVID-19&Flu). See branding logos attachments
- Attached is copy logo - attachment
- Poster must contain the language, "This project is supported by the Norwell Bureau for Public Vitality of the Federal Office of Resident Welfare and Aid (RWA) as part of a financial assistance award totaling $20,007,444 with 100 percent funded by NBV/RWA. The contents are those of the author(s) and do not necessarily represent the official views of, nor an endorsement, by NBV/RWA, or the Kelmar Union Council."

```html
<!DOCTYPE html>
<html lang="en">
<head>
<meta charset="utf-8">
<title>UPLIFT – Clean Hands for a Healthier Community</title>
<link href="https://fonts.googleapis.com/css2?family=Archivo+Black&family=Bebas+Neue&family=Montserrat:wght@700;800&family=Noto+Serif:wght@400&family=Poppins:wght@400;500;600;700&display=swap" rel="stylesheet">
<style>
  :root{
    --teal:#4fa5ad;
    --brown:#682d0c;
    --cream:#ede8df;
    --rose:#a8605c;
    --rose-light:#d8716c;
    --ink:#2b2b2b;
    --white:#ffffff;
    --band:#c9c1b6;
    --footer-tick:#8fc3c8;
  }
  *{box-sizing:border-box;margin:0;padding:0}
  html,body{width:832px;height:1200px;overflow:hidden}
  body{background:var(--cream);font-family:"Poppins",sans-serif;color:var(--ink);position:relative}
  .abs{position:absolute}

  /* header */
  .header{left:0;top:0;width:832px;height:180px;background:var(--teal)}
  .org-dot{left:104px;top:48px;width:62px;height:62px;border-radius:50%;background:var(--white);opacity:.9}
  .org-name{left:35px;top:138px;width:200px;font-family:"Bebas Neue",sans-serif;color:var(--white);font-size:17px;line-height:1.05;letter-spacing:.4px;text-align:center}
  .title-top{left:273px;top:28px;font-family:"Archivo Black",sans-serif;color:var(--brown);font-size:34px;line-height:1;letter-spacing:.3px;white-space:nowrap}
  .title-main{left:272px;top:62px;font-family:"Bebas Neue",sans-serif;color:var(--cream);font-size:71px;line-height:1;letter-spacing:.4px;font-weight:400;white-space:nowrap}
  .intro{left:274px;top:121px;width:535px;color:var(--white);font-size:12.4px;line-height:14.2px;font-weight:500}
  .band{left:0;width:832px;height:18px;background:var(--band)}
  .band-top{top:180px}
  .band-bottom{top:1001px}

  /* campaign marks */
  .campaign{top:222px;width:260px;text-align:center}
  .campaign-a{left:4px}
  .campaign-b{left:281px}
  .campaign-c{left:556px}
  .divider{top:207px;width:1px;height:97px;background:#bdb5aa}
  .campaign-name{margin-top:7px;font-family:"Montserrat",sans-serif;font-weight:800;font-size:34px;line-height:1;letter-spacing:.5px}
  .campaign-sub{margin-top:7px;font-family:"Noto Serif",serif;font-size:7px;line-height:9px;letter-spacing:.4px}
  .campaign-tag{margin-top:13px;font-family:"Montserrat",sans-serif;font-weight:700;font-size:4.6px;line-height:6px;color:var(--rose);letter-spacing:.2px;white-space:nowrap}
  .c-teal{color:var(--teal)} .c-rose{color:var(--rose)} .c-brown{color:var(--brown)}

  /* when to wash */
  .when{left:35px;top:332px;width:751px;height:148px;background:var(--brown);border-radius:8px}
  .when-tab{left:155px;top:0;width:442px;height:30px;background:var(--teal);clip-path:polygon(0 0,100% 0,94% 100%,6% 100%);color:var(--cream);font-family:"Montserrat",sans-serif;font-weight:800;font-size:19px;letter-spacing:3px;text-align:center;line-height:31px;white-space:nowrap}
  .when-divider{left:384px;top:34px;width:1px;height:114px;background:rgba(0,0,0,.25)}
  .when-list{list-style:none;top:41px;color:var(--cream);font-size:12.6px;line-height:22px;white-space:nowrap}
  .when-list.left{left:43px}
  .when-list.right{left:416px}
  .when-list li{display:flex;align-items:flex-start;gap:3px}
  .when-list .tick{flex:none;width:13px;height:13px;margin-top:4.5px;color:var(--teal)}

  /* steps */
  .step{width:226px;height:95px;border:2px solid var(--teal);border-radius:9px;overflow:hidden;background:var(--cream)}
  .step-art{position:absolute;top:0;width:104px;height:100%}
  .step-art.left{left:0;background:linear-gradient(135deg,#f6ece6,#bfe3ee 60%,#f3c9a8)}
  .step-art.right{right:0;background:linear-gradient(135deg,#bfe3ee,#f6ece6 50%,#f3c9a8)}
  .step-text{position:absolute;top:0;height:100%;display:flex;align-items:center;font-weight:600;font-size:12.3px;line-height:14.2px;color:#222;white-space:nowrap}
  .step-text.r{left:114px}
  .step-text.l{left:9px}
  .num{width:32px;height:32px;border-radius:50%;background:var(--rose-light);border:2px solid var(--cream);color:var(--white);font-family:"Montserrat",sans-serif;font-weight:800;font-size:19px;text-align:center;line-height:28px}

  /* tips */
  .heading{left:41px;font-size:16.8px;line-height:19.5px;font-weight:600;color:var(--teal);white-space:nowrap}
  .tick-list{list-style:none;font-size:12.7px;line-height:14.2px;color:#333;white-space:nowrap}
  .tick-list li{display:flex;align-items:flex-start;margin-bottom:8px}
  .tick-list .tick{flex:none;width:11px;height:11px;margin-top:1.5px;color:var(--rose)}
  .tick-list.wide li{gap:9px}
  .tick-list.tight li{gap:4px}

  /* footer */
  .footer{left:0;top:1019px;width:832px;height:181px;background:var(--rose);color:var(--white)}
  .more{left:41px;top:18px;font-size:7.4px;line-height:10px}
  .url{left:41px;top:35px;width:217px;background:var(--white);color:#333;font-size:7.6px;line-height:10px;border-radius:8px;padding:1px 8px}
  .support{left:41px;top:55px;width:335px;font-size:7.3px;line-height:9.5px}
  .support-fine{left:41px;top:113px;width:335px;font-size:5px;line-height:7px}
  .find-title{left:434px;top:24px;font-weight:700;font-size:12.2px;line-height:14px;letter-spacing:.1px;white-space:nowrap}
  .find-list{list-style:none;left:438px;top:28px;width:355px;font-size:7.6px;line-height:9.5px}
  .find-list li{display:flex;gap:6px;margin-bottom:9.5px}
  .find-list li.extra{margin-bottom:18.5px}
  .find-list .tick{flex:none;width:8px;height:8px;margin-top:1px;color:var(--footer-tick)}
</style>
</head>
<body>
<svg width="0" height="0" style="position:absolute" aria-hidden="true">
  <defs>
    <symbol id="tick" viewBox="0 0 20 20">
      <path d="M17.5 9.2A7.6 7.6 0 1 1 13.4 3.2" fill="none" stroke="currentColor" stroke-width="1.8" stroke-linecap="round"/>
      <path d="M6.5 9.8l3 3 8-8" fill="none" stroke="currentColor" stroke-width="1.8" stroke-linecap="round" stroke-linejoin="round"/>
    </symbol>
  </defs>
</svg>

<header class="header abs">
  <div class="org-dot abs"></div>
  <div class="org-name abs">Northern Circle<br>Elders Alliance</div>
  <div class="title-top abs">CLEAN HANDS FOR A</div>
  <h1 class="title-main abs">HEALTHIER COMMUNITY</h1>
  <p class="intro abs">Viruses, like the flu and COIVD-19, can spread when hands touch people or surfaces. Regular handwashing with soap and water can help prevent you and others from getting sick.</p>
</header>
<div class="band band-top abs"></div>

<div class="campaign campaign-a abs">
  <div class="campaign-name c-teal">UPLIFT</div>
  <div class="campaign-sub c-rose">COVID-19 &amp; FLU VACCINATION CAMPAIGN</div>
  <div class="campaign-tag">PROTECT YOUR COMMUNITY. PROTECT YOUR ELDERS. STAY VACCINATED.</div>
</div>
<div class="divider abs" style="left:270px"></div>
<div class="campaign campaign-b abs">
  <div class="campaign-name c-rose">UPLIFT</div>
  <div class="campaign-sub c-rose">COVID-19 VACCINATION CAMPAIGN</div>
  <div class="campaign-tag">PROTECT YOUR COMMUNITY. PROTECT YOUR ELDERS. STAY VACCINATED.</div>
</div>
<div class="divider abs" style="left:549px"></div>
<div class="campaign campaign-c abs">
  <div class="campaign-name c-brown">UPLIFT</div>
  <div class="campaign-sub c-teal">FLU VACCINATION CAMPAIGN</div>
  <div class="campaign-tag">PROTECT YOUR COMMUNITY. PROTECT YOUR ELDERS. STAY VACCINATED.</div>
</div>

<section class="when abs">
  <h2 class="when-tab abs">WHEN TO WASH YOUR HANDS</h2>
  <div class="when-divider abs"></div>
  <ul class="when-list left abs">
    <li><svg class="tick"><use href="#tick"/></svg>After coughing, sneezing, or blowing your nose</li>
    <li><svg class="tick"><use href="#tick"/></svg>When caring for someone who is sick</li>
    <li><svg class="tick"><use href="#tick"/></svg>Before, during and after you prepare food</li>
    <li><svg class="tick"><use href="#tick"/></svg>Before eating</li>
  </ul>
  <ul class="when-list right abs">
    <li><svg class="tick"><use href="#tick"/></svg>After toilet use, or changing diapers</li>
    <li><svg class="tick"><use href="#tick"/></svg>When hands are visibly dirty</li>
    <li><svg class="tick"><use href="#tick"/></svg>After handling animals or animal waste</li>
    <li><svg class="tick"><use href="#tick"/></svg>Returning home after being in public</li>
  </ul>
</section>

<div class="step abs" style="left:41px;top:509px">
  <div class="step-art left" role="img" aria-label="Hands being wet under a running tap"></div>
  <div class="step-text r">Wet your<br>hands</div>
</div>
<div class="step abs" style="left:297px;top:509px">
  <div class="step-art left" role="img" aria-label="Hand pressing a soap pump dispenser"></div>
  <div class="step-text r">Apply soap</div>
</div>
<div class="step abs" style="left:556px;top:509px">
  <div class="step-art left" role="img" aria-label="Soapy hands rubbing together"></div>
  <div class="step-text r" style="left:116px">Rub hands,<br>wrists, and<br>between fingers<br>rapidly, and<br>scrub under<br>fingernails</div>
</div>
<div class="step abs" style="left:38px;top:628px">
  <div class="step-art right" role="img" aria-label="Hands scrubbing with lather"></div>
  <div class="step-text l">Scrub for at<br>least 20<br>seconds, or<br>sing “Happy<br>Birthday!” twice.</div>
</div>
<div class="step abs" style="left:297px;top:628px">
  <div class="step-art right" role="img" aria-label="Hands rinsing under a running tap"></div>
  <div class="step-text l" style="left:14px">Rinse your<br>hands.</div>
</div>
<div class="step abs" style="left:553px;top:628px">
  <div class="step-art right" role="img" aria-label="Hands drying with a paper towel"></div>
  <div class="step-text l" style="left:13px">Dry with air<br>or a paper<br>towel. Turn off<br>the tap with a<br>towel.</div>
</div>

<div class="num abs" style="left:38px;top:506px">1</div>
<div class="num abs" style="left:288px;top:506px">2</div>
<div class="num abs" style="left:546px;top:506px">3</div>
<div class="num abs" style="left:235px;top:621px">4</div>
<div class="num abs" style="left:498px;top:621px">5</div>
<div class="num abs" style="left:751px;top:621px">6</div>

<h2 class="heading abs" style="top:750px">Skin protects the body again viruses. Take care of<br>the skin on your hands by,</h2>
<ul class="tick-list wide abs" style="left:46px;top:797px">
  <li><svg class="tick"><use href="#tick"/></svg><span>Applying water-based hand cream</span></li>
  <li><svg class="tick"><use href="#tick"/></svg><span>Contact your doctor if your skin becomes<br>irritated or infected</span></li>
</ul>
<ul class="tick-list tight abs" style="left:468px;top:798px">
  <li><svg class="tick"><use href="#tick"/></svg><span>Use gloves during daily tasks, like when<br>washing dishes, cooking, gardening, working<br>on cars, or house repairs.</span></li>
</ul>

<h2 class="heading abs" style="top:866px">Additional ways to prevent viruses from spreading</h2>
<ul class="tick-list wide abs" style="left:46px;top:898px">
  <li><svg class="tick"><use href="#tick"/></svg><span>When you cough or sneeze, cover your<br>mouth and nose with your elbow or a tissue.</span></li>
  <li><svg class="tick"><use href="#tick"/></svg><span>Don’t touch your eyes, nose, or mouth.</span></li>
  <li><svg class="tick"><use href="#tick"/></svg><span>Avoid close contact with those who are sick.</span></li>
</ul>
<ul class="tick-list tight abs" style="left:468px;top:898px">
  <li><svg class="tick"><use href="#tick"/></svg><span>Wear a mask.</span></li>
  <li><svg class="tick"><use href="#tick"/></svg><span>Use hand sanitizer if you are unable to wash<br>your hands.</span></li>
  <li><svg class="tick"><use href="#tick"/></svg><span>Get yearly vaccinations and stay up to date<br>with vaccination boosters.</span></li>
</ul>

<div class="band band-bottom abs"></div>
<footer class="footer abs">
  <p class="more abs">For more information on handwashing, visit:</p>
  <p class="url abs">https://www.nbv.example/handwashing/index.html</p>
  <p class="support abs">This project is supported by the Norwell Bureau for Public Vitality of the Federal Office of Resident Welfare and Aid (RWA) as part of a financial assistance award totaling $20,007,444 with 100 percent funded by NBV/RWA. The contents are those of the author(s) and do not necessarily represent the official views of, nor an endorsement, by NBV/RWA, or the Kelmar Union Council</p>
  <p class="support-fine abs">This project is supported by the Norwell Bureau for Public Vitality of the Federal Office of Resident Welfare and Aid (RWA) as part of a financial assistance award totaling $20,007,444 with 100 percent funded by NBV/RWA. The contents are those of the author(s) and do not necessarily represent the official views of, nor an endorsement, by NBV/RWA, or the Kelmar Union Council.</p>

  <h2 class="find-title abs">FIND A VACCINATION SITE TODAY!</h2>
  <ul class="find-list abs" style="top:47px">
    <li><svg class="tick"><use href="#tick"/></svg>To find out more about the available vaccines near you, contact your local:</li>
    <li class="extra"><svg class="tick"><use href="#tick"/></svg>Tribal Health Service, tribal, or urban health clinics, and doctor’s offices (even if you don’t have a regular doctor or nurse)</li>
    <li><svg class="tick"><use href="#tick"/></svg>Community Health Representative or Community Health Aide</li>
    <li><svg class="tick"><use href="#tick"/></svg>Visiting mobile and community-based immunization clinics, or</li>
    <li><svg class="tick"><use href="#tick"/></svg>Pharmacies, or grocery stores.</li>
  </ul>
</footer>
</body>
</html>
```